Brennick Framing Company - Card Design

I am looking to use the logo designs that you already did for me to develop a business card. I would like the card to have a black background and be double sided. I want white and green logo and text. I have attached an inspiration photo of a look that I like. I would like to use the Vertical Logo attached to take up the full front side of the card. On the back where I have my name and information, I would like to have the horizontal logo or maybe even just the image of the 'A' and trees without the text. I am open, but I am looking for something clean and simple and I want the green to really pop! Additional files can be found under Design #: 64093528

Target Market(s)

Homeowners

Industry/Entity Type

Construction

Contact Information for Business Card

Name: Marcus Brennick, Title: Project Manager, Phone: 647.382.9105, Email: brennickframingcompany@quillpost.example, address: 418 Larkspur Ln, Calderwood, CA 90417, Lic# 5836214

Colors
00AB8E
00BBA5
67D7C9
C6EFE9
E9F9F6

Requirements
Nice to have
• I would like to see the logos that I have already got from ArtSwarm, though I am open to new ones

```html
<!DOCTYPE html>
<html lang="en">
<head>
<meta charset="utf-8">
<title>Brennick Framing Company – Business Card</title>
<link rel="stylesheet" href="https://fonts.googleapis.com/css2?family=Montserrat:wght@400;500;700&display=swap">
<style>
  :root {
    --stage: #3a3a3c;
    --card-light: #3b3637;
    --card-dark: #1f1c1d;
    --green: #5bb848;
    --green-deep: #44a233;
    --white: #ffffff;
    --silver: #b9b9bb;
  }
  * { box-sizing: border-box; margin: 0; padding: 0; }
  html, body {
    width: 1200px; height: 1200px; overflow: hidden;
    background: var(--stage);
    font-family: "Montserrat", sans-serif;
  }
  .sheet {
    width: 1200px; height: 1200px;
    display: flex; flex-direction: column; align-items: center; justify-content: center;
    gap: 60px;
  }
  .card {
    position: relative;
    width: 840px; height: 480px;
    background: radial-gradient(ellipse at 50% 35%, var(--card-light) 0%, var(--card-dark) 80%);
    box-shadow: 0 18px 40px rgba(0,0,0,.45);
    overflow: hidden;
  }

  /* Logo side */
  .card--logo { display: flex; align-items: center; justify-content: center; }
  .logo-lockup { display: flex; align-items: center; gap: 22px; }
  .logo-lockup__dot {
    width: 54px; height: 54px; border-radius: 50%;
    border: 3px solid var(--silver);
  }
  .logo-lockup__name {
    color: var(--silver);
    font-weight: 700; font-size: 36px; letter-spacing: 2px;
    text-transform: uppercase;
  }

  /* Info side */
  .brand {
    position: absolute; left: 60px; top: 56px;
    color: var(--white); font-weight: 700; font-size: 30px;
    letter-spacing: 1px; text-transform: uppercase;
    display: flex; align-items: center; gap: 16px;
  }
  .brand__dot { width: 34px; height: 34px; border-radius: 50%; background: var(--green); }
  .contact {
    position: absolute; left: 60px; top: 150px;
    color: var(--white); font-size: 17px; line-height: 1.55;
    list-style: none;
  }
  .contact li { display: flex; align-items: flex-start; gap: 10px; }
  .contact__icon { width: 16px; height: 16px; margin-top: 5px; flex: none; }
  .contact__text--indent { padding-left: 26px; }
  .person {
    position: absolute; right: 110px; top: 320px; text-align: right;
  }
  .person__name { color: var(--green); font-weight: 700; font-size: 38px; line-height: 1.2; }
  .person__title { color: var(--white); font-size: 19px; margin-top: 4px; }

  .edge { position: absolute; right: 0; width: 34px; }
  .edge--top { top: 0; height: 205px; background: var(--green); border-bottom-left-radius: 14px; }
  .edge--mark { top: 228px; height: 58px; background: var(--white); border-radius: 10px 0 0 10px; }
  .edge--bottom { top: 309px; bottom: 0; background: var(--green-deep); border-top-left-radius: 14px; }
</style>
</head>
<body>
<main class="sheet">

  <section class="card card--logo" aria-label="Card front">
    <div class="logo-lockup">
      <span class="logo-lockup__dot"></span>
      <span class="logo-lockup__name">Brennick Framing Company</span>
    </div>
  </section>

  <section class="card card--info" aria-label="Card back">
    <div class="brand">
      <span class="brand__dot"></span>
      <span>Brennick Framing Company</span>
    </div>

    <ul class="contact">
      <li><span class="contact__text--indent">418 Larkspur Ln, Calderwood,<br>CA 90417</span></li>
      <li>
        <svg class="contact__icon" viewBox="0 0 16 16" aria-hidden="true">
          <path fill="#5bb848" d="M3.6 1.5l2.2 2.6-1.3 1.6c.8 1.9 2.2 3.3 4.1 4.1l1.6-1.3 2.6 2.2-1.4 2.4C6.7 12.8 3.2 9.3 1.2 4.6z"/>
        </svg>
        <span>647.382.9105</span>
      </li>
      <li>
        <svg class="contact__icon" viewBox="0 0 16 16" aria-hidden="true">
          <rect x="1" y="3" width="14" height="10" rx="1" fill="#5bb848"/>
          <path d="M1.5 3.8L8 8.8l6.5-5" fill="none" stroke="#1f1c1d" stroke-width="1.3"/>
        </svg>
        <span>brennickframingcompany@quillpost.example</span>
      </li>
      <li><span>Lic# 5836214</span></li>
    </ul>

    <div class="person">
      <p class="person__name">Marcus Brennick</p>
      <p class="person__title">Project Manager</p>
    </div>

    <span class="edge edge--top"></span>
    <span class="edge edge--mark"></span>
    <span class="edge edge--bottom"></span>
  </section>

</main>
</body>
</html>
```